Calloway Ridge Associates Stationery

Use attached logo for stationery
Stationery, Letterhead and Envelope + Business cards

Tag line: Walking alongside those doing the work of the Gospel

```html
<!DOCTYPE html>
<html lang="en">
<head>
<meta charset="utf-8">
<title>Calloway Ridge Associates Stationery</title>
<link href="https://fonts.googleapis.com/css2?family=Cinzel:wght@600&family=Montserrat:wght@400;600;700&display=swap" rel="stylesheet">
<style>
  :root{
    --navy:#2c2a6b;
    --navy-dark:#221f57;
    --gold:#f6c21c;
    --paper:#ffffff;
    --backdrop:#e6e4e2;
    --ink:#2c2a6b;
    --muted:#6b6a8e;
  }
  *{box-sizing:border-box;margin:0;padding:0}
  html,body{width:1200px;height:2416px;overflow:hidden}
  body{background:var(--backdrop);font-family:'Montserrat',sans-serif;color:var(--ink);position:relative}

  .brand{display:flex;flex-direction:column;align-items:center;gap:6px}
  .brand-row{display:flex;align-items:center;gap:10px}
  .brand-dot{width:16px;height:16px;border-radius:50%;background:var(--gold);flex:none}
  .brand-name{font-family:'Cinzel',serif;font-weight:600;letter-spacing:1px;line-height:1.05;text-align:center}
  .brand-tag{font-size:9px;letter-spacing:.3px;text-align:center}

  /* business card back */
  .card-back{position:absolute;left:300px;top:60px;width:600px;height:340px;background:var(--navy);display:flex;align-items:center;justify-content:center}
  .card-back .brand-name{color:var(--paper);font-size:34px}
  .card-back .brand-tag{color:var(--paper);opacity:.85;font-size:11px}

  /* business card front */
  .card-front{position:absolute;left:300px;top:440px;width:600px;height:340px;background:var(--paper);overflow:hidden}
  .card-front svg.shape{position:absolute;inset:0}
  .card-front .brand{position:absolute;left:36px;top:46px;align-items:flex-start}
  .card-front .brand-name{color:var(--navy);font-size:22px;text-align:left}
  .card-front .brand-tag{color:var(--muted);text-align:left;font-size:8px}
  .holder-name{position:absolute;right:40px;top:70px;color:var(--paper);font-weight:700;font-size:22px;letter-spacing:1px}
  .contacts{position:absolute;left:36px;top:178px;display:flex;flex-direction:column;gap:9px;font-size:13px;color:var(--navy);font-weight:600}
  .contact{display:flex;align-items:center;gap:8px}
  .contact svg{width:16px;height:16px;flex:none}
  .card-front .email{position:absolute;left:36px;top:276px;font-size:13px;color:var(--paper);font-weight:600;display:flex;align-items:center;gap:8px}
  .card-front .email svg{width:16px;height:16px}

  /* letterhead */
  .letterhead{position:absolute;left:340px;top:860px;width:520px;height:735px;background:var(--paper);box-shadow:0 2px 6px rgba(0,0,0,.08)}
  .letterhead .brand{position:absolute;right:34px;top:34px}
  .letterhead .brand-name{color:var(--navy);font-size:14px}
  .letterhead .brand-dot{width:10px;height:10px}
  .letterhead .brand-tag{font-size:5px;color:var(--muted)}
  .letterhead .band{position:absolute;left:0;right:0;bottom:0;height:54px;background:var(--navy);border-top:4px solid var(--gold);display:flex;align-items:center;justify-content:center;gap:26px;color:var(--paper);font-size:9px}
  .band .contact svg{width:11px;height:11px}

  /* envelope */
  .envelope{position:absolute;left:150px;top:1870px;width:900px;height:420px;background:var(--paper);overflow:hidden;box-shadow:0 2px 6px rgba(0,0,0,.08)}
  .envelope .brand{position:absolute;left:50px;top:150px;align-items:flex-start}
  .envelope .brand-name{color:var(--navy);font-size:26px;text-align:left}
  .envelope .brand-tag{color:var(--muted);text-align:left;font-size:9px}
  .envelope .stripe{position:absolute;left:0;right:0;top:268px;height:12px;background:var(--gold)}
  .envelope .band{position:absolute;left:0;right:0;top:280px;bottom:0;background:var(--navy);color:var(--paper);font-size:14px;padding:26px 50px;display:grid;grid-template-columns:auto 1fr;gap:14px 50px;align-content:start}
  .envelope .band .contact svg{width:16px;height:16px}
</style>
</head>
<body>

<svg width="0" height="0" style="position:absolute">
  <defs>
    <symbol id="icon-phone" viewBox="0 0 16 16"><circle cx="8" cy="8" r="8" fill="currentColor"/><path d="M5.2 4.2l1.6-.3.8 2-1 .8a5.5 5.5 0 0 0 2.7 2.7l.8-1 2 .8-.3 1.6c-3.6.3-6.9-3-6.6-6.6z" fill="#fff"/></symbol>
    <symbol id="icon-web" viewBox="0 0 16 16"><circle cx="8" cy="8" r="8" fill="currentColor"/><circle cx="8" cy="8" r="4.5" fill="none" stroke="#fff" stroke-width="1"/><path d="M3.5 8h9M8 3.5c-2 2.5-2 6.5 0 9M8 3.5c2 2.5 2 6.5 0 9" fill="none" stroke="#fff" stroke-width="1"/></symbol>
    <symbol id="icon-mail" viewBox="0 0 16 16"><circle cx="8" cy="8" r="8" fill="currentColor"/><rect x="4" y="5.2" width="8" height="5.6" fill="none" stroke="#fff" stroke-width="1"/><path d="M4 5.4l4 3 4-3" fill="none" stroke="#fff" stroke-width="1"/></symbol>
  </defs>
</svg>

<section class="card-back">
  <div class="brand">
    <div class="brand-row"><span class="brand-dot"></span><span class="brand-name">Calloway Ridge<br>Associates</span></div>
    <p class="brand-tag">Walking alongside those doing the work of the Gospel</p>
  </div>
</section>

<section class="card-front">
  <svg class="shape" viewBox="0 0 600 340" preserveAspectRatio="none">
    <polygon points="330,0 600,0 600,200 330,200" fill="var(--navy)"/>
    <polygon points="0,262 600,222 600,250 0,300" fill="var(--gold)"/>
    <polygon points="0,300 600,250 600,340 0,340" fill="var(--navy)"/>
  </svg>
  <div class="brand">
    <div class="brand-row"><span class="brand-dot"></span><span class="brand-name">Calloway Ridge<br>Associates</span></div>
    <p class="brand-tag">Walking alongside those doing the work of the Gospel</p>
  </div>
  <p class="holder-name">YOUR NAME</p>
  <div class="contacts">
    <span class="contact"><svg style="color:var(--navy)"><use href="#icon-phone"/></svg>041 27 38 90</span>
    <span class="contact"><svg style="color:var(--navy)"><use href="#icon-web"/></svg>www.callowayridge.com</span>
  </div>
  <p class="email"><svg style="color:var(--gold)"><use href="#icon-mail"/></svg>hello@callowayridge.com</p>
</section>

<section class="letterhead">
  <div class="brand">
    <div class="brand-row"><span class="brand-dot"></span><span class="brand-name">Calloway Ridge<br>Associates</span></div>
    <p class="brand-tag">Walking alongside those doing the work of the Gospel</p>
  </div>
  <div class="band">
    <span class="contact"><svg style="color:var(--gold)"><use href="#icon-phone"/></svg>041 27 38 90</span>
    <span class="contact"><svg style="color:var(--gold)"><use href="#icon-web"/></svg>www.callowayridge.com</span>
    <span class="contact"><svg style="color:var(--gold)"><use href="#icon-mail"/></svg>hello@callowayridge.com</span>
  </div>
</section>

<section class="envelope">
  <div class="brand">
    <div class="brand-row"><span class="brand-dot"></span><span class="brand-name">Calloway Ridge<br>Associates</span></div>
    <p class="brand-tag">Walking alongside those doing the work of the Gospel</p>
  </div>
  <div class="stripe"></div>
  <div class="band">
    <span class="contact"><svg style="color:var(--gold)"><use href="#icon-phone"/></svg>041 27 38 90</span>
    <span class="contact"><svg style="color:var(--gold)"><use href="#icon-web"/></svg>www.callowayridge.com</span>
    <span class="contact"><svg style="color:var(--gold)"><use href="#icon-mail"/></svg>hello@callowayridge.com</span>
  </div>
</section>

</body>
</html>
```